Brochure Projecct

I need a brochure created for my company, which will be sent to customers via email in PDF format. I have uploaded the company logo with this project, which I want incorporated in the design.

Designers should view the company website at www.brightcounselpages.com. I want the brochure to compliment the website (i.e., very clean design). I would also like pictures added to the brochure to make the design visually stunning.

In terms of content, I need four pages in the brochure to add four separate sections of content (one section per page). The four sections of content will be as follows (1) Search Engine Optimization Benefits (2) Increased Client Retention (3) Showcase Your Law Firm (4) Maximize Your Online ROI (5) Pricing Plans. I will give the content to the winning designer to add to the project. Each individual content section will have four subsection titles after which content of approximately 100 to 200 words will appear.

Designers can decide if other pages should be added to the brochure (i.e., a "cover page" that would have little content, but be visually appealing like the cover of a book - - - a "back page" that may just have the logo, contact information, etc).

My company address and email address should be prominently featured through every page (address: 2715 West Juniper Avenue, Suite 1400, Scottsdale, Arizona 85317; email: sales@brightcounselpages.com).

Industry/Entity Type

It Company

Requirements
Must have
• Clean look but visually stunning incorporating the design of the website at brightcounselpages.com as well as the logo. Also, room for content as set forth in the description of this project.

```html
<!DOCTYPE html>
<html lang="en">
<head>
<meta charset="utf-8">
<title>Bright Counsel Pages – Brochure Cover</title>
<link href="https://fonts.googleapis.com/css2?family=Open+Sans:wght@300;400;600;700&family=Roboto+Condensed:wght@400;700&display=swap" rel="stylesheet">
<style>
  :root {
    --stage: #ecebe8;
    --ink-black: #050505;
    --menu-brown: #2a2720;
    --menu-line: #5a5648;
    --sky: #2bb8ee;
    --sky-light: #45c8f5;
    --ocean: #0a63a8;
    --paper: #ffffff;
    --mist: #c9c9c9;
  }
  * { box-sizing: border-box; margin: 0; padding: 0; }
  html, body { width: 1200px; height: 900px; overflow: hidden; background: var(--stage); }
  body { position: relative; font-family: "Open Sans", Arial, sans-serif; }

  .spread { position: absolute; left: 62px; top: 72px; width: 1098px; height: 776px;
    box-shadow: 0 4px 16px rgba(0,0,0,.25); }
  .cover { position: absolute; top: 0; height: 776px; overflow: hidden; }
  .cover--back { left: 0; width: 548px; background: var(--ink-black); }
  .cover--front { left: 548px; width: 550px; background: var(--ink-black); }

  .photo { position: absolute; }

  /* back cover */
  .brand-mark { position: absolute; left: 40px; top: 150px; display: flex; align-items: center; gap: 16px; }
  .brand-mark__dot { width: 46px; height: 46px; border-radius: 50%; background: var(--sky); }
  .brand-mark__name { font-weight: 700; font-size: 34px; line-height: 1.05; color: var(--paper); }

  .photo--stamp { left: 378px; top: 26px; width: 170px; height: 142px; border-radius: 12px 0 0 12px;
    background: linear-gradient(180deg, #3a3d46 0%, #6b6e78 35%, #d9dadd 62%, #f6f6f6 100%); }

  .search-head { position: absolute; left: 376px; top: 198px; width: 148px; height: 55px;
    background: linear-gradient(#4a4a4a, #262626); border-radius: 6px 6px 0 0;
    display: flex; align-items: center; gap: 10px; padding-left: 14px; }
  .search-head__dot { width: 30px; height: 30px; border-radius: 50%; background: var(--sky); }
  .search-head__text { color: var(--paper); font-size: 13px; line-height: 1.15; font-weight: 300; letter-spacing: .5px; }
  .search-head__text b { font-size: 16px; font-weight: 400; }

  .practice-list { position: absolute; left: 376px; top: 263px; width: 148px; list-style: none;
    background: var(--menu-brown); }
  .practice-list li { color: var(--paper); font-size: 10.5px; text-align: center; line-height: 1.2;
    height: 21.7px; display: flex; align-items: center; justify-content: center;
    border-bottom: 1px solid var(--menu-line); }
  .practice-list li.tall { height: 33px; }
  .practice-list li:last-child { border-bottom: 0; }

  .photo--team { left: 0; top: 322px; width: 368px; height: 232px;
    background:
      linear-gradient(180deg, rgba(5,5,5,1) 0%, rgba(5,5,5,0) 30%, rgba(5,5,5,0) 78%, rgba(12,12,16,.9) 100%),
      linear-gradient(90deg, #9fb8d8 0%, #c9d3df 35%, #eeeeee 55%, #b9c8dc 80%, #7d6655 100%); }

  .ribbon { position: absolute; top: 556px; height: 32px; display: flex; align-items: center;
    font-weight: 300; font-size: 22px; letter-spacing: 3px; color: var(--paper); }
  .ribbon--state { left: 0; width: 200px; padding-left: 34px; color: #06283f;
    background: linear-gradient(90deg, var(--sky-light), var(--sky));
    clip-path: polygon(0 0, 100% 0, 93% 100%, 0 100%); }
  .ribbon--services { left: 196px; width: 262px; padding-left: 24px;
    background: linear-gradient(90deg, #4e4e4e, #2c2c2c);
    clip-path: polygon(6% 0, 100% 0, 94% 100%, 0 100%); }

  .contact { position: absolute; right: 256px; top: 632px; text-align: right; color: var(--mist);
    font-size: 8.5px; line-height: 1.5; font-style: normal; }
  .contact__email { margin-top: 8px; }
  .contact__email b { color: var(--paper); font-weight: 700; }
  .site-link { position: absolute; left: 21px; top: 694px; color: var(--sky); font-size: 17px; letter-spacing: 1.4px; }

  .photo--lens { left: 305px; top: 603px; width: 243px; height: 138px; border-radius: 12px 0 0 12px;
    background: linear-gradient(135deg, #ededed 0%, #c4c4c4 45%, #8a8a8a 75%, #cfcfcf 100%); }

  .tile-strip { position: absolute; left: 0; top: 750px; width: 548px; height: 14px; display: flex; gap: 6px; padding-left: 4px; }
  .tile-strip span { width: 18px; height: 14px; border-radius: 3px; background: linear-gradient(#555, #262626); }

  /* front cover */
  .masthead { position: absolute; left: 0; top: 0; width: 550px; height: 178px;
    background: linear-gradient(90deg, #c9c9c9 0%, #f4f4f4 35%, #ffffff 100%);
    display: flex; align-items: center; justify-content: center; gap: 14px; }
  .masthead__dot { width: 40px; height: 40px; border-radius: 50%; background: var(--ocean); }
  .masthead__name { font-weight: 700; font-size: 30px; color: #111; }

  .hero { position: absolute; left: 0; top: 178px; width: 550px; height: 378px; }

  .band { position: absolute; left: 0; top: 556px; width: 550px; height: 220px;
    background: linear-gradient(90deg, #44c9f6 0%, #2aa6e3 50%, #0b5aa3 100%); }

  .front-ribbon { position: absolute; left: 196px; top: 556px; width: 330px; height: 32px; z-index: 2;
    background: linear-gradient(90deg, #3c3c3c, #1f1f1f);
    clip-path: polygon(5% 0, 100% 0, 95% 100%, 0 100%);
    color: var(--paper); font-size: 15.5px; letter-spacing: 1.3px;
    display: flex; align-items: center; padding-left: 28px; }

  .photo--counsel { left: 0; top: 601px; width: 126px; height: 139px; border-radius: 0 12px 12px 0; z-index: 1;
    background: linear-gradient(180deg, #7a3a22 0%, #9c5a38 30%, #d8bfa6 55%, #3a3a40 85%, #2a2a30 100%); }

  .tagline { position: absolute; right: 216px; top: 680px; text-align: right; color: var(--paper);
    font-weight: 300; font-size: 27px; line-height: 1.25; letter-spacing: 1px; z-index: 1; }
  .divider { position: absolute; left: 357px; top: 625px; width: 1px; height: 116px; background: rgba(255,255,255,.85); z-index: 1; }
  .headline { position: absolute; left: 378px; top: 622px; color: var(--paper); z-index: 1;
    font-family: "Roboto Condensed", "Arial Narrow", sans-serif; font-weight: 700; text-align: center;
    line-height: 1.02; letter-spacing: 1px; }
  .headline span { display: block; }
  .headline .l1 { font-size: 31px; }
  .headline .l2 { font-size: 45px; }
  .headline .l3 { font-size: 31px; }
</style>
</head>
<body>
  <main class="spread">
    <section class="cover cover--back" aria-label="Back cover">
      <div class="brand-mark">
        <span class="brand-mark__dot"></span>
        <span class="brand-mark__name">Bright<br>Counsel Pages</span>
      </div>

      <div class="photo photo--stamp" role="img" aria-label="Photo of a lawyer's hands stamping a document at a desk"></div>

      <div class="search-head">
        <span class="search-head__dot"></span>
        <span class="search-head__text">you can<br><b>SEARCH</b></span>
      </div>
      <ul class="practice-list">
        <li>Family Lawyer</li>
        <li>Personal Injury Lawyers</li>
        <li class="tall">Social Security &amp;<br>Workers Comp</li>
        <li>Business Lawyers</li>
        <li>Taxation Lawyers</li>
        <li>Real Estate Lawyers</li>
        <li>Employment Lawyers</li>
        <li>Mediation Lawyers</li>
        <li>Estate Planning Lawyers</li>
        <li>Bankruptcy Lawyers</li>
        <li>Criminal Defense Lawyers</li>
        <li>Intellectual Property</li>
      </ul>

      <div class="photo photo--team" role="img" aria-label="Group photo of six smiling legal professionals in light shirts"></div>

      <div class="ribbon ribbon--state">ARIZONA</div>
      <div class="ribbon ribbon--services">LEGAL SERVICES</div>

      <address class="contact">
        <div>2715 West Juniper Avenue,</div>
        <div>Suite 1400, Scottsdale, Arizona 85317</div>
        <div class="contact__email"><b>email:</b> sales@brightcounselpages.com</div>
      </address>
      <div class="site-link">www.brightcounselpages.com</div>

      <div class="photo photo--lens" role="img" aria-label="Photo of a magnifying glass resting on printed pages"></div>

      <div class="tile-strip" aria-hidden="true">
        <span></span><span></span><span></span><span></span><span></span><span></span><span></span><span></span>
        <span></span><span></span><span></span><span></span><span></span><span></span><span></span><span></span>
        <span></span><span></span><span></span><span></span><span></span><span></span>
      </div>
    </section>

    <section class="cover cover--front" aria-label="Front cover">
      <header class="masthead">
        <span class="masthead__dot"></span>
        <span class="masthead__name">Bright Counsel Pages</span>
      </header>

      <svg class="hero" viewBox="0 0 550 378" width="550" height="378">
        <defs>
          <linearGradient id="libraryTone" x1="0" y1="0" x2="0" y2="1">
            <stop offset="0" stop-color="#1e1410"/>
            <stop offset=".45" stop-color="#35241a"/>
            <stop offset=".75" stop-color="#5a3a22"/>
            <stop offset="1" stop-color="#8a5426"/>
          </linearGradient>
          <linearGradient id="officeTone" x1="0" y1="0" x2="0" y2="1">
            <stop offset="0" stop-color="#3a2620"/>
            <stop offset=".35" stop-color="#c9ab96"/>
            <stop offset=".6" stop-color="#2c2a30"/>
            <stop offset="1" stop-color="#1c1c22"/>
          </linearGradient>
        </defs>
        <rect width="550" height="378" fill="url(#libraryTone)" role="img" aria-label="Photo of golden scales of justice before shelves of law books"/>
        <polygon points="462,0 550,0 550,378 292,378" fill="#0b4f8c"/>
        <polygon points="474,0 550,0 550,378 306,378" fill="url(#officeTone)" role="img" aria-label="Photo of a smiling lawyer typing at a desk"/>
      </svg>

      <div class="band"></div>
      <div class="front-ribbon">www.brightcounselpages.com</div>

      <div class="photo photo--counsel" role="img" aria-label="Photo of a lawyer reading in a law library"></div>

      <div class="tagline">LOCAL<br>DIRECTORY OF</div>
      <div class="divider"></div>
      <h1 class="headline">
        <span class="l1">ARIZONA</span>
        <span class="l2">LEGAL</span>
        <span class="l3">SERVICES</span>
      </h1>
    </section>
  </main>
</body>
</html>
```